TARO PTY LTD - Business Cards

Design a modern business card - using the attached Designs.
Same design as on the front, apart from the names/numbers/emails to be different.
We want the cards to be very glossy to stand out, do I think the simple black/white/metallic will be effective.
Both lots of details below:

Lyle Marrick
Director
lyle_taro@quintmail.example
0493 628 304

Simon Prowle
Director
simon_taro@quintmail.example
0438 514 209

```html
<!DOCTYPE html>
<html lang="en">
<head>
<meta charset="utf-8">
<title>TARO PTY LTD – Business Cards</title>
<link rel="stylesheet" href="https://fonts.googleapis.com/css2?family=Arimo:wght@400;700&display=swap">
<style>
  :root {
    --page-bg: #d9d9d9;
    --metal-light: #e4e4e4;
    --metal-mid: #b9b9b9;
    --metal-dark: #8a8a8a;
    --band-black: #121212;
    --band-stripe: #3a3a3a;
    --rail-light: #9a9a9a;
    --rail-dark: #2a2a2a;
    --rivet: #dcdcdc;
    --ink: #262626;
    --badge-dark: #2b2f33;
  }
  * { box-sizing: border-box; margin: 0; padding: 0; }
  html, body { width: 1200px; height: 1000px; overflow: hidden; }
  body {
    background: var(--page-bg);
    font-family: "Arimo", Arial, sans-serif;
    position: relative;
  }
  .card {
    position: absolute;
    left: 328px;
    width: 545px;
    height: 312px;
    overflow: hidden;
    background:
      linear-gradient(115deg, var(--metal-dark) 0%, var(--metal-light) 22%, var(--metal-mid) 40%, var(--metal-light) 55%, var(--metal-dark) 75%, var(--metal-light) 100%);
    box-shadow: 0 4px 14px rgba(0,0,0,0.25);
  }
  .card--lyle { top: 150px; }
  .card--simon { top: 540px; }
  .card-band {
    position: absolute;
    left: 0; top: 0;
    width: 100%; height: 45px;
    background:
      repeating-linear-gradient(120deg, var(--band-black) 0 48px, var(--band-stripe) 48px 58px, var(--band-black) 58px 70px);
  }
  .card-rail {
    position: absolute;
    left: 0; top: 45px;
    width: 100%; height: 32px;
    background: linear-gradient(180deg, var(--rail-dark) 0%, var(--rail-light) 45%, var(--rail-dark) 100%);
  }
  .rivet {
    position: absolute;
    top: 10px;
    width: 12px; height: 12px;
    border-radius: 50%;
    background: radial-gradient(circle at 35% 35%, #ffffff, var(--rivet) 45%, #6b6b6b);
  }
  .rivet--left { left: 10px; }
  .rivet--right { right: 10px; }
  .brand {
    position: absolute;
    left: 0; top: 100px;
    width: 100%; height: 110px;
    display: flex;
    align-items: center;
    justify-content: center;
    gap: 12px;
  }
  .brand-disc {
    flex: none;
    width: 44px; height: 44px;
    border-radius: 50%;
    background: var(--badge-dark);
  }
  .brand-name {
    font-family: "Arimo", Arial, sans-serif;
    font-weight: 700;
    font-size: 26px;
    letter-spacing: 1px;
    color: var(--ink);
    white-space: nowrap;
  }
  .contact {
    position: absolute;
    left: 33px; top: 252px;
    font-size: 17px;
    line-height: 21px;
    color: var(--ink);
  }
  .phone {
    position: absolute;
    right: 37px; top: 273px;
    font-size: 17px;
    line-height: 21px;
    color: var(--ink);
  }
</style>
</head>
<body>
  <section class="card card--lyle">
    <div class="card-band"></div>
    <div class="card-rail">
      <span class="rivet rivet--left"></span>
      <span class="rivet rivet--right"></span>
    </div>
    <div class="brand">
      <span class="brand-disc"></span>
      <span class="brand-name">TARO PTY LTD</span>
    </div>
    <div class="contact">
      <p class="contact-name">Lyle Marrick Director</p>
      <p class="contact-email">lyle_taro@quintmail.example</p>
    </div>
    <p class="phone">0493 628 304</p>
  </section>

  <section class="card card--simon">
    <div class="card-band"></div>
    <div class="card-rail">
      <span class="rivet rivet--left"></span>
      <span class="rivet rivet--right"></span>
    </div>
    <div class="brand">
      <span class="brand-disc"></span>
      <span class="brand-name">TARO PTY LTD</span>
    </div>
    <div class="contact">
      <p class="contact-name">Simon Prowle Director</p>
      <p class="contact-email">simon_taro@quintmail.example</p>
    </div>
    <p class="phone">0438 514 209</p>
  </section>
</body>
</html>
```